Wine labels Velmora Wine Council - Nueva etiqueta El Consejo Regulador de vinos de Albarrán

Velmora Wines Council, based in southern Spain, are looking to create a new suite of wine labels which retain the elegance of the Velmora Wines industry while reinvigorating their image to the modern era and a new generation of Sherry Wine lovers. These labels will be used across the Velmora Wines Council's range of wines for the promotion of the Velmora Wines industry.

Your design must present at least two styles of Velmora Wines which demonstrate an elegant, modern interpretation and understanding of the unique mood and personality for these wines and the essence of southern Spain.

10 labels will be created based on the winning design, one for each of the unique varieties of Velmora Wines within the collection. This collection comprises of several different wine varieties including: Fino, Manzanilla, Amontillado, Oloroso, Palo Cortado, Medium, Cream, Pale Cream, Pedro Ximenez and Moscatel.

We recommend you visit our website www.velmora-vinos.example/wines as the source to understanding the origins and unique personality of these diverse wines.

El Consejo Regulador de los Vinos de Albarrán y Tordesal quiere renovar las etiquetas de los vinos utilizados para sus actividades de promoción genérica. Esta colección de vinos comprende las tipologías más importantes de la región que incluye: fino, manzanilla, amontillado, oloroso, palo cortado, pale cream, medium, cream, pedro ximénez y moscatel. Por lo tanto se precisan 10 etiquetas, una para cada uno de los vinos mencionados.
Updates

Project Deadline Extended
Reason: Due to some confusion with the deadline we wish to officially extend the deadline to allow designers one last week to submit their entries.

Target Market(s)

Industry, journalists, media, sommeliers, chefs, wine writers

Industry/Entity Type

Council

Requirements
Must have
• Front and Back label plus capsule:
• Front label can have either of the two official logos of the Velmora Wine council titled Vinos de Albarrán Digital or not, this is optional. Must include: Vino selecionado por el Consejo Regulador de la Denominacion de Origen, Name of the variety of wine eg FINO, percentage of alcohol eg 15% and quantity 75 cl.
• The back of the label must include the council logo titled Sellora and 4 additional logos positioned smaller. The Europa logo must appear larger than the 3 other logos. Space for descriptive text about the wine is also required.
• The dimensions of the bottle can be found at this link http://www.vidrialto.example/es/catalogo/vinos-y-espumosos/bordelesas/bd-orla
• Altura:305 mm
• Diámetro base:76,20 mm
• Diámetro hombro:82 mm
• Tipo boca:Cetie
• Peso:750 gr
• Capacidad:75 cl
• Etiqueta delantera y trasera y capsula
• La etiqueta delantera puede incluir el logo oficial del Consejo Regulador o el logo digital, o ninguno, esto es opcional. Debe incluir el siguiete texto: Vino selecionado por el Consejo Regulador de la Denominacion de Origen, el nombre de la variedad del vino, por ejemplo Fino, el porcentaje de alcohol, por ejemplo 15%, y la capacidad 75cl.
• La etiqueta trasera debe incluir el logo oficial Sellora del Consejo, y cuatro logos adicionales con una dimension menor. El Logo de ¨Europa invierte en las zonas rurales¨ debe ser de mayor tamaño que los otros. Se precisa espacio para el texto descriptivo de los vinos.
• Las dimensiones de la botella se puede encontrar en este enlace
• http://www.vidrialto.example/es/catalogo/vinos-y-espumosos/bordelesas/bd-orla
• Altura:305 mm
• Diámetro base:76,20 mm
• Diámetro hombro:82 mm
• Tipo boca:Cetie
• Peso:750 gr
• Capacidad:75 cl
Nice to have
• See our website velmora-vinos.example to understand the origin of the wines. Ver nuestra página web velmora-vinos.example para mejor entender los vinos.
Should not have
• Images of catavinos or stereotypical images from Spain such as flamenco dancers or guitars.

```html
<!DOCTYPE html>
<html lang="es">
<head>
<meta charset="utf-8">
<title>Vinos de Albarrán — Etiquetas</title>
<link rel="stylesheet" href="https://fonts.googleapis.com/css2?family=Cormorant+Garamond:wght@500&family=Jost:wght@400;500&display=swap">
<style>
  :root {
    --bg: #0b1a2e;
    --paper: #fbfaf7;
    --crimson: #b8164a;
    --ink: #2a2320;
    --red: #c2261a;
    --teal: #2aa3c0;
    --gold: #c9a24a;
    --soft-text: #d7dde6;
  }
  * { box-sizing: border-box; margin: 0; padding: 0; }
  html, body { width: 1200px; height: 1200px; overflow: hidden; }
  body {
    background: var(--bg);
    font-family: "Jost", sans-serif;
  }
  .label-suite {
    position: absolute;
    inset: 0;
    display: grid;
    grid-template-columns: repeat(5, 196px);
    grid-template-rows: repeat(2, 400px);
    column-gap: 36px;
    row-gap: 150px;
    padding: 125px 38px 0;
  }
  .front-label-set { display: flex; flex-direction: column; align-items: center; }
  .front-label {
    position: relative;
    width: 196px;
    height: 350px;
    text-align: center;
    color: var(--ink);
  }
  .label-shape { position: absolute; inset: 0; width: 100%; height: 100%; }
  .label-shape path { fill: var(--paper); }
  .front-label--px .label-shape path { fill: var(--crimson); }
  .front-label--px { color: #fff; }
  .label-body { position: relative; padding-top: 42px; }
  .brand-name {
    font-family: "Cormorant Garamond", serif;
    font-weight: 500;
    font-size: 14px;
    letter-spacing: 0.5px;
  }
  .brand-sub {
    font-size: 5.5px;
    letter-spacing: 2px;
    margin-top: 1px;
  }
  .ornament {
    display: block;
    width: 140px;
    height: 140px;
    margin: 16px auto 0;
    border-radius: 50%;
  }
  .variety-name {
    font-weight: 500;
    font-size: 15.5px;
    letter-spacing: 1.6px;
    margin-top: 26px;
    line-height: 1.15;
  }
  .variety-name .initial { color: var(--red); }
  .front-label--manzanilla .initial { color: var(--teal); }
  .front-label--px .initial { color: var(--gold); font-style: italic; }
  .front-label--px .variety-name { margin-top: 14px; }
  .origin-note {
    font-size: 7px;
    line-height: 1.25;
    margin-top: 12px;
  }
  .origin-note .council { font-size: 8.5px; display: block; }
  .origin-note .do { font-size: 5px; display: block; }
  .volume-line {
    margin-top: 14px;
    font-family: "Cormorant Garamond", serif;
    font-size: 10px;
    color: var(--soft-text);
    display: flex;
    align-items: center;
    gap: 5px;
  }
  .volume-line .dot { width: 6px; height: 6px; border-radius: 50%; background: var(--soft-text); }
  .orn-px { background: radial-gradient(circle, #e8c86a 0%, #c99a3a 45%, rgba(184,22,74,0) 72%); }
  .orn-manzanilla { background: radial-gradient(circle, #7fd0e2 0%, #2aa3c0 55%, rgba(42,163,192,0) 72%); }
  .orn-fino { background: radial-gradient(circle, #e7b95a 0%, #c8572a 50%, rgba(200,87,42,0) 72%); }
  .orn-amontillado { background: radial-gradient(circle, #e6b458 0%, #a85a25 50%, rgba(168,90,37,0) 72%); }
  .orn-oloroso { background: radial-gradient(circle, #e9c25e 0%, #b8862f 52%, rgba(184,134,47,0) 72%); }
  .orn-palo { background: radial-gradient(circle, #e8b45c 0%, #b33a22 52%, rgba(179,58,34,0) 72%); }
  .orn-pale { background: radial-gradient(circle, #d25a33 0%, #a8231a 50%, rgba(168,35,26,0) 72%); }
  .orn-medium { background: radial-gradient(circle, #c9803c 0%, #a0281a 52%, rgba(160,40,26,0) 72%); }
  .orn-cream { background: radial-gradient(circle, #d8853e 0%, #9b2a18 50%, rgba(155,42,24,0) 72%); }
  .orn-moscatel { background: radial-gradient(circle, #d8404a 0%, #b01f2a 50%, rgba(176,31,42,0) 72%); }
</style>
</head>
<body>
<main class="label-suite">

  <section class="front-label-set">
    <div class="front-label front-label--px">
      <svg class="label-shape" viewBox="0 0 196 350" preserveAspectRatio="none"><path d="M0 22 C40 6 80 4 120 14 C150 22 175 18 196 10 V340 Q196 350 186 350 H10 Q0 350 0 340 Z"/></svg>
      <div class="label-body">
        <p class="brand-name">VINOS DE ALBARRÁN</p>
        <p class="brand-sub">VELMORA WINES</p>
        <div class="ornament orn-px" role="img" aria-label="Ornamento dorado con hoja de vid sobre fondo carmesí"></div>
        <h2 class="variety-name">PEDRO<br><span class="initial">X</span>IMÉNEZ</h2>
        <p class="origin-note">Vino selecionado por el<span class="council">Consejo Regulador</span><span class="do">de la Denominacion de Origen</span></p>
      </div>
    </div>
    <p class="volume-line">75cl <span class="dot"></span> 15% vol.</p>
  </section>

  <section class="front-label-set">
    <div class="front-label front-label--manzanilla">
      <svg class="label-shape" viewBox="0 0 196 350" preserveAspectRatio="none"><path d="M0 22 C40 6 80 4 120 14 C150 22 175 18 196 10 V340 Q196 350 186 350 H10 Q0 350 0 340 Z"/></svg>
      <div class="label-body">
        <p class="brand-name">VINOS DE ALBARRÁN</p>
        <p class="brand-sub">VELMORA WINES</p>
        <div class="ornament orn-manzanilla" role="img" aria-label="Roseta ornamental en azul turquesa"></div>
        <h2 class="variety-name"><span class="initial">M</span>ANZANILLA</h2>
        <p class="origin-note">Vino selecionado por el<span class="council">Consejo Regulador</span><span class="do">de la Denominacion de Origen</span></p>
      </div>
    </div>
    <p class="volume-line">75cl <span class="dot"></span> 15% vol.</p>
  </section>

  <section class="front-label-set">
    <div class="front-label">
      <svg class="label-shape" viewBox="0 0 196 350" preserveAspectRatio="none"><path d="M0 22 C40 6 80 4 120 14 C150 22 175 18 196 10 V340 Q196 350 186 350 H10 Q0 350 0 340 Z"/></svg>
      <div class="label-body">
        <p class="brand-name">VINOS DE ALBARRÁN</p>
        <p class="brand-sub">VELMORA WINES</p>
        <div class="ornament orn-fino" role="img" aria-label="Ornamento en oro y rojo"></div>
        <h2 class="variety-name"><span class="initial">F</span>INO</h2>
        <p class="origin-note">Vino selecionado por el<span class="council">Consejo Regulador</span><span class="do">de la Denominacion de Origen</span></p>
      </div>
    </div>
    <p class="volume-line">75cl <span class="dot"></span> 15% vol.</p>
  </section>

  <section class="front-label-set">
    <div class="front-label">
      <svg class="label-shape" viewBox="0 0 196 350" preserveAspectRatio="none"><path d="M0 22 C40 6 80 4 120 14 C150 22 175 18 196 10 V340 Q196 350 186 350 H10 Q0 350 0 340 Z"/></svg>
      <div class="label-body">
        <p class="brand-name">VINOS DE ALBARRÁN</p>
        <p class="brand-sub">VELMORA WINES</p>
        <div class="ornament orn-amontillado" role="img" aria-label="Ornamento romboidal en oro y ámbar"></div>
        <h2 class="variety-name"><span class="initial">A</span>MONTILLADO</h2>
        <p class="origin-note">Vino selecionado por el<span class="council">Consejo Regulador</span><span class="do">de la Denominacion de Origen</span></p>
      </div>
    </div>
    <p class="volume-line">75cl <span class="dot"></span> 15% vol.</p>
  </section>

  <section class="front-label-set">
    <div class="front-label">
      <svg class="label-shape" viewBox="0 0 196 350" preserveAspectRatio="none"><path d="M0 22 C40 6 80 4 120 14 C150 22 175 18 196 10 V340 Q196 350 186 350 H10 Q0 350 0 340 Z"/></svg>
      <div class="label-body">
        <p class="brand-name">VINOS DE ALBARRÁN</p>
        <p class="brand-sub">VELMORA WINES</p>
        <div class="ornament orn-oloroso" role="img" aria-label="Medallón ornamental dorado"></div>
        <h2 class="variety-name"><span class="initial">O</span>LOROSO</h2>
        <p class="origin-note">Vino selecionado por el<span class="council">Consejo Regulador</span><span class="do">de la Denominacion de Origen</span></p>
      </div>
    </div>
    <p class="volume-line">75cl <span class="dot"></span> 15% vol.</p>
  </section>

  <section class="front-label-set">
    <div class="front-label">
      <svg class="label-shape" viewBox="0 0 196 350" preserveAspectRatio="none"><path d="M0 22 C40 6 80 4 120 14 C150 22 175 18 196 10 V340 Q196 350 186 350 H10 Q0 350 0 340 Z"/></svg>
      <div class="label-body">
        <p class="brand-name">VINOS DE ALBARRÁN</p>
        <p class="brand-sub">VELMORA WINES</p>
        <div class="ornament orn-palo" role="img" aria-label="Roseta ornamental en oro y rojo"></div>
        <h2 class="variety-name"><span class="initial">P</span>ALO CORTADO</h2>
        <p class="origin-note">Vino selecionado por el<span class="council">Consejo Regulador</span><span class="do">de la Denominacion de Origen</span></p>
      </div>
    </div>
    <p class="volume-line">75cl <span class="dot"></span> 15% vol.</p>
  </section>

  <section class="front-label-set">
    <div class="front-label">
      <svg class="label-shape" viewBox="0 0 196 350" preserveAspectRatio="none"><path d="M0 22 C40 6 80 4 120 14 C150 22 175 18 196 10 V340 Q196 350 186 350 H10 Q0 350 0 340 Z"/></svg>
      <div class="label-body">
        <p class="brand-name">VINOS DE ALBARRÁN</p>
        <p class="brand-sub">VELMORA WINES</p>
        <div class="ornament orn-pale" role="img" aria-label="Ornamento horizontal en rojo"></div>
        <h2 class="variety-name"><span class="initial">P</span>ALE CREAM</h2>
        <p class="origin-note">Vino selecionado por el<span class="council">Consejo Regulador</span><span class="do">de la Denominacion de Origen</span></p>
      </div>
    </div>
    <p class="volume-line">75cl <span class="dot"></span> 15% vol.</p>
  </section>

  <section class="front-label-set">
    <div class="front-label">
      <svg class="label-shape" viewBox="0 0 196 350" preserveAspectRatio="none"><path d="M0 22 C40 6 80 4 120 14 C150 22 175 18 196 10 V340 Q196 350 186 350 H10 Q0 350 0 340 Z"/></svg>
      <div class="label-body">
        <p class="brand-name">VINOS DE ALBARRÁN</p>
        <p class="brand-sub">VELMORA WINES</p>
        <div class="ornament orn-medium" role="img" aria-label="Ornamento en forma de arco en rojo y oro"></div>
        <h2 class="variety-name"><span class="initial">M</span>EDIUM</h2>
        <p class="origin-note">Vino selecionado por el<span class="council">Consejo Regulador</span><span class="do">de la Denominacion de Origen</span></p>
      </div>
    </div>
    <p class="volume-line">75cl <span class="dot"></span> 15% vol.</p>
  </section>

  <section class="front-label-set">
    <div class="front-label">
      <svg class="label-shape" viewBox="0 0 196 350" preserveAspectRatio="none"><path d="M0 22 C40 6 80 4 120 14 C150 22 175 18 196 10 V340 Q196 350 186 350 H10 Q0 350 0 340 Z"/></svg>
      <div class="label-body">
        <p class="brand-name">VINOS DE ALBARRÁN</p>
        <p class="brand-sub">VELMORA WINES</p>
        <div class="ornament orn-cream" role="img" aria-label="Ornamento vertical en rojo oscuro"></div>
        <h2 class="variety-name"><span class="initial">C</span>REAM</h2>
        <p class="origin-note">Vino selecionado por el<span class="council">Consejo Regulador</span><span class="do">de la Denominacion de Origen</span></p>
      </div>
    </div>
    <p class="volume-line">75cl <span class="dot"></span> 15% vol.</p>
  </section>

  <section class="front-label-set">
    <div class="front-label">
      <svg class="label-shape" viewBox="0 0 196 350" preserveAspectRatio="none"><path d="M0 22 C40 6 80 4 120 14 C150 22 175 18 196 10 V340 Q196 350 186 350 H10 Q0 350 0 340 Z"/></svg>
      <div class="label-body">
        <p class="brand-name">VINOS DE ALBARRÁN</p>
        <p class="brand-sub">VELMORA WINES</p>
        <div class="ornament orn-moscatel" role="img" aria-label="Ilustración de racimo de uvas rojas con hojas de vid"></div>
        <h2 class="variety-name"><span class="initial">M</span>OSCATEL</h2>
        <p class="origin-note">Vino selecionado por el<span class="council">Consejo Regulador</span><span class="do">de la Denominacion de Origen</span></p>
      </div>
    </div>
    <p class="volume-line">75cl <span class="dot"></span> 15% vol.</p>
  </section>

</main>
</body>
</html>
```